Real Estate Agent need a business card

I am a real estate agent in Vancouver, BC Canada. I recently used PixelHarbor to develop a logo of my own. I would like to have my logo in the business card, as well my realty office logo also must be displayed along with its address. I also would like to have my headshot photo displayed in the business card on both sides.

Industry/Entity Type

Real Estate Agent

Contact Information for Business Card

My office address:
Bramwell Peak Realty
2271 Lindqvist St.
Vancouver, BC V5K 2P8

My contact information:
Cell: 604-555-0148
Office: 604-555-0192
Fax: 604-555-0193

My website : www.danielmorvik.example
My email: email@danielmorvik.example

My slogan: Simply I do. Far and Above.

Requirements
Must have
• Front side(all in colour): My photo, My own logo, My office logo, My cell number, My website address and email, My slogan.
• Back side(could be black & white/ plz refer to the file name "preview"): My photo, My own logo, my office logo, my office address, my contact information.
• * Please read this: Since my logo has my name in it, there is no need to put my name in the card separately. As well, my office logo MUST BE displayed on both sides(you can reduce the size of office logo). But the office address can be displayed only one side, front or back. I would prefer to have my cell number only to be displayed prominently on the front side. So all the numbers should be displayed on the backside instead. Remember that I am trying to promote myself so the most important thing I consider from the front side of the card is my cell number, my website, and my email, not the office. The only thing I require by industry regulation from the front side is my office logo. Hope this helps.
Nice to have
• Colour on the front side and the black and white on the back side

```html
<!DOCTYPE html>
<html lang="en">
<head>
<meta charset="utf-8">
<title>Daniel Morvik – Business Card</title>
<link href="https://fonts.googleapis.com/css2?family=Open+Sans:wght@400;600;700&display=swap" rel="stylesheet">
<style>
  :root{
    --bg:#e9e9e7;
    --ink:#0d0d0d;
    --panel:#161616;
    --panel-soft:#202020;
    --green:#7fd321;
    --green-deep:#5fb012;
    --white:#ffffff;
    --paper:#f3f3f3;
    --text-dark:#2a2a2a;
    --text-soft:#cfcfcf;
    --line:#3a3a3a;
  }
  *{box-sizing:border-box;margin:0;padding:0}
  html,body{width:1200px;height:801px;overflow:hidden}
  body{
    background:var(--bg);
    font-family:"Open Sans",Arial,sans-serif;
    position:relative;
  }
  .card{
    position:absolute;
    top:246px;
    width:540px;height:309px;
    background:var(--paper);
    overflow:hidden;
    box-shadow:0 6px 18px rgba(0,0,0,.18);
  }
  .card--back{left:40px}
  .card--front{left:620px}

  .green-strip{position:absolute;left:0;top:0;width:100%;height:14px;background:var(--green)}

  /* agent name lockup */
  .agent-mark{display:flex;align-items:center;gap:8px}
  .agent-mark__square{width:16px;height:16px;background:var(--green);flex:none}
  .agent-mark__name{color:var(--white);font-weight:600;font-size:15px;letter-spacing:1.5px;text-transform:uppercase;line-height:1;white-space:nowrap}
  .agent-role{color:var(--green);font-size:7.5px;font-weight:600;letter-spacing:1.6px;text-transform:uppercase;margin-top:4px;padding-left:24px}

  .office-mark{color:var(--white);font-size:10px;font-weight:400;letter-spacing:1px;text-transform:uppercase;text-align:center;line-height:1.3}

  .headshot{
    position:absolute;background:var(--white);padding:5px;
    box-shadow:0 2px 6px rgba(0,0,0,.35);
  }
  .headshot__fill{width:100%;height:100%;background:linear-gradient(160deg,#c9b58a 0%,#8e9aa6 45%,#2c3440 100%)}

  .label{color:var(--green-deep);font-weight:700}

  /* back card */
  .card--back .dark-area{
    position:absolute;left:0;top:14px;width:100%;height:138px;
    background:linear-gradient(135deg,var(--panel) 0%,var(--ink) 60%,var(--panel-soft) 100%);
  }
  .card--back .lower-area{
    position:absolute;left:0;top:152px;width:100%;height:157px;
    background:linear-gradient(160deg,#ffffff 0%,#ececec 55%,#f8f8f8 100%);
  }
  .card--back .headshot{left:50px;top:72px;width:118px;height:118px}
  .card--back .agent-block{position:absolute;left:198px;top:108px}
  .card--back .office-mark{position:absolute;left:400px;top:40px;width:120px}
  .office-address{
    position:absolute;left:50px;top:208px;
    font-size:11px;line-height:1.65;color:var(--text-dark);white-space:nowrap;
  }
  .office-address__name{font-weight:700;text-transform:uppercase;letter-spacing:.8px}
  .office-numbers{
    position:absolute;left:300px;top:208px;
    font-size:11px;line-height:1.65;color:var(--text-dark);white-space:nowrap;
  }

  /* front card */
  .card--front .dark-area{
    position:absolute;left:0;top:14px;width:100%;height:208px;background:var(--ink);
  }
  .card--front .dark-side{
    position:absolute;right:0;top:14px;width:200px;height:208px;
    background:linear-gradient(150deg,var(--panel-soft),var(--ink));
  }
  .card--front .agent-block{position:absolute;left:22px;top:34px}
  .card--front .divider{position:absolute;left:22px;top:78px;width:300px;height:1px;background:var(--line)}
  .card--front .office-mark{position:absolute;left:40px;top:100px;width:140px}
  .slogan{
    position:absolute;left:22px;top:176px;width:320px;
    color:var(--text-soft);font-size:11px;letter-spacing:.6px;
  }
  .slogan__accent{color:var(--green);font-weight:600}
  .card--front .headshot{left:380px;top:78px;width:118px;height:118px}
  .contact{
    position:absolute;left:22px;top:232px;width:500px;
    color:var(--text-dark);white-space:nowrap;
  }
  .contact__cell{font-size:16px;font-weight:700;line-height:1.4;letter-spacing:.4px}
  .contact__row{font-size:11px;line-height:1.9}
</style>
</head>
<body>

  <section class="card card--back" aria-label="Card back">
    <div class="green-strip"></div>
    <div class="dark-area"></div>
    <div class="lower-area" role="img" aria-label="Soft white faceted background texture"></div>
    <div class="headshot"><div class="headshot__fill" role="img" aria-label="Agent headshot photo"></div></div>
    <div class="agent-block">
      <div class="agent-mark"><span class="agent-mark__square"></span><span class="agent-mark__name">Daniel Morvik</span></div>
      <div class="agent-role">Real Estate Agent</div>
    </div>
    <div class="office-mark">Bramwell Peak Realty</div>
    <div class="office-address">
      <div class="office-address__name">Bramwell Peak Realty</div>
      <div>2271 Lindqvist St.</div>
      <div>Vancouver, BC V5K 2P8</div>
    </div>
    <div class="office-numbers">
      <div><span class="label">Cell</span> : 604-555-0148</div>
      <div><span class="label">Office</span> : 604-555-0192</div>
      <div><span class="label">Fax</span> : 604-555-0193</div>
    </div>
  </section>

  <section class="card card--front" aria-label="Card front">
    <div class="green-strip"></div>
    <div class="dark-area"></div>
    <div class="dark-side"></div>
    <div class="agent-block">
      <div class="agent-mark"><span class="agent-mark__square"></span><span class="agent-mark__name">Daniel Morvik</span></div>
      <div class="agent-role">Real Estate Agent</div>
    </div>
    <div class="divider"></div>
    <div class="office-mark">Bramwell Peak Realty</div>
    <div class="slogan">Simply I do. <span class="slogan__accent">Far and Above.</span></div>
    <div class="headshot"><div class="headshot__fill" role="img" aria-label="Agent headshot photo"></div></div>
    <div class="contact">
      <div class="contact__cell"><span class="label">Cell</span> : 604-555-0148</div>
      <div class="contact__row"><span class="label">Web</span> : www.danielmorvik.example &nbsp;&nbsp;<span class="label">Email</span> : email@danielmorvik.example</div>
    </div>
  </section>

</body>
</html>
```